Business Cards for a Dating Coach/Social Dynamics company
Velvet Compass
Professional
Ted
Dating Instructor
4872 Marlow Terrace, #9
Miami Beach, FL 33139
Skyheron@velvetcompasslife.com
www.velvetcompasslife.com

```html
<!DOCTYPE html>
<html lang="en">
<head>
<meta charset="utf-8">
<title>Velvet Compass — Business Cards</title>
<link href="https://fonts.googleapis.com/css2?family=Raleway:wght@400;600&display=swap" rel="stylesheet">
<style>
  :root {
    --page: #e9e9e9;
    --card: #505052;
    --text: #f2f2f2;
    --muted: #c9c9c9;
    --red: #d52a1e;
    --orange: #f08a1c;
    --silver: #7a7a7c;
  }
  * { margin: 0; padding: 0; box-sizing: border-box; }
  html, body { width: 1200px; height: 1009px; overflow: hidden; }
  body {
    background: var(--page);
    font-family: "Raleway", sans-serif;
    color: var(--text);
    position: relative;
  }
  .card {
    position: absolute;
    left: 250px;
    width: 700px;
    height: 400px;
    background: var(--card);
    border-radius: 22px;
    overflow: hidden;
    box-shadow: 0 6px 18px rgba(0,0,0,.18);
  }
  .card--front { top: 54px; }
  .card--back { top: 544px; }

  .accent-band {
    position: absolute;
    left: 0; right: 0; bottom: 0;
    height: 72px;
    background: linear-gradient(180deg, var(--red) 0, var(--orange) 10px, var(--silver) 22px, #6a6a6c 100%);
  }

  .brand {
    position: absolute;
    display: flex;
    align-items: center;
    gap: 12px;
  }
  .brand__mark {
    width: 30px; height: 30px;
    border-radius: 50%;
    background: var(--red);
  }
  .brand__name {
    font-weight: 600;
    color: var(--red);
    letter-spacing: .5px;
  }
  .card--front .brand { left: 150px; top: 92px; }
  .card--front .brand__name { font-size: 34px; }
  .tagline {
    position: absolute;
    left: 192px; top: 142px;
    font-size: 11px;
    letter-spacing: 2.2px;
    color: var(--muted);
    text-transform: uppercase;
  }

  .address {
    position: absolute;
    left: 60px; top: 205px;
    font-size: 15px;
    font-style: normal;
    line-height: 1.55;
    color: var(--text);
  }

  .person {
    position: absolute;
    left: 400px; top: 190px;
  }
  .person__name { font-size: 16px; font-weight: 600; color: var(--red); }
  .person__role { font-size: 13px; color: var(--text); margin-bottom: 10px; }
  .contact { list-style: none; font-size: 12px; line-height: 1.85; color: var(--text); }
  .contact li { display: flex; align-items: center; gap: 8px; }
  .contact svg { width: 13px; height: 13px; flex: none; }

  .card--back .brand {
    left: 0; right: 0; top: 150px;
    justify-content: center;
  }
  .card--back .brand__mark { width: 44px; height: 44px; }
  .card--back .brand__name { font-size: 40px; }
  .website {
    position: absolute;
    left: 0; right: 0; top: 228px;
    text-align: center;
    font-size: 13px;
    letter-spacing: 3px;
    color: var(--muted);
  }
  .website span { color: var(--red); }
</style>
</head>
<body>

<section class="card card--front" aria-label="Business card front">
  <div class="brand">
    <span class="brand__mark"></span>
    <span class="brand__name">Velvet Compass</span>
  </div>
  <p class="tagline">Lifestyle and Dating Specialists</p>

  <address class="address">
    4872 Marlow Terrace, #9<br>
    Miami Beach, FL 33139
  </address>

  <div class="person">
    <p class="person__name">Ted</p>
    <p class="person__role">Dating Instructor</p>
    <ul class="contact">
      <li>
        <svg viewBox="0 0 16 16"><circle cx="8" cy="8" r="8" fill="var(--red)"/><path d="M5 4.5l1.5-.5 1 2-1 .8a5 5 0 0 0 2.7 2.7l.8-1 2 1-.5 1.5c-3.5 0-6.5-3-6.5-6.5z" fill="#fff"/></svg>
        305 555 0142
      </li>
      <li>
        <svg viewBox="0 0 16 16"><circle cx="8" cy="8" r="8" fill="var(--red)"/><rect x="4" y="5" width="8" height="6" fill="#fff"/><path d="M4 5l4 3.2L12 5" stroke="var(--red)" fill="none"/></svg>
        Skyheron@velvetcompasslife.com
      </li>
      <li>
        <svg viewBox="0 0 16 16"><circle cx="8" cy="8" r="8" fill="var(--red)"/><circle cx="8" cy="8" r="4" fill="none" stroke="#fff" stroke-width="1.3"/><path d="M4 8h8M8 4v8" stroke="#fff" stroke-width="1"/></svg>
        www.velvetcompasslife.com
      </li>
    </ul>
  </div>

  <div class="accent-band" role="img" aria-label="Decorative red, orange and silver wave band"></div>
</section>

<section class="card card--back" aria-label="Business card back">
  <div class="brand">
    <span class="brand__mark"></span>
    <span class="brand__name">Velvet Compass</span>
  </div>
  <p class="website">www.<span>velvetcompasslife</span>.com</p>
</section>

</body>
</html>
```